Striking new Advert required for Commercial Real Estate Agency

We need a a NEW newspaper advertisement for the marketing of a large commercial property (a Backpackers lodge)

Dimensions are to be width of 101mm and height of 100mm (10cms)

Our key design statement for this advert is clean, modern and minimalist design, with accents of 'HOT PINK' colour to remove it from looking too boring, perhaps in the area of the contact icons. The heirachy of the advert is outlined in the attached ADVERTISEMENT TEXT FILE.

Our company name is THE VANTREL COLLECTIVE, and we want our brand to appear professional yet classy in it's design style (sort of like an advertising or design agency)

We have two logo options below, one more square in its layout (which we prefer) and the other more rectangular, which may be better suited for the layout. We are not adverse to the logo being reversed (white text on black), along with other key element areas such as the main advert heading and the "FOR SALE" part, and think this would be a good option.
There are two photos attached to be included in the advert.

We have attached an example of an old advert that we did, which we DID NOT LIKE, and which was for a smaller width than the one we need (it is only 65% of the width of this one). WE have also atached a file showing layout of some of our competitors adverts, which we dont think are too good either.

We are really open for ideas, but have time pressures, so please come back with any questions as soon as you can, if needed.

Thank you
Updates

Thank you for the great and diverse designs. There are a few standout options, but one style that we prefer most.

Target Market(s)

We are wanting this newspaper advertisement to attract interest from real estat e developers, investors and motel/lodge owners, along with other high nett worth individuals

Industry/Entity Type

Real Estate

Font styles to use
Serif
Sans Serif

Colors
1b1b1b
a54499
474747
fbfbfb

Requirements
Must have
• Clean modern look, predominantly monochromatic or black and white, with the hot pink accent somewhere, as mentioned above.
• All the contents of the TEXT provided, perhaps with additional space to add a little more if needed, Please advise if you think we dont have enough space for all of the TEXT
Should not have
• Script like fonts
• Cartoonish characters
• a 'cheap' look

```html
<!DOCTYPE html>
<html lang="en">
<head>
<meta charset="utf-8">
<title>Mount Victoria Land Grab – For Sale</title>
<link href="https://fonts.googleapis.com/css2?family=Montserrat:wght@500;600;800&family=Roboto+Condensed:wght@400;700&display=swap" rel="stylesheet">
<style>
  :root {
    --ink: #1b1b1b;
    --panel: #231f20;
    --pink: #b0197f;
    --grey: #474747;
    --paper: #ffffff;
    --backdrop: #ececec;
  }
  * { margin: 0; padding: 0; box-sizing: border-box; }
  html, body { width: 1200px; height: 1000px; overflow: hidden; background: var(--backdrop); }
  .advert {
    position: absolute; left: 158px; top: 72px; width: 885px; height: 874px;
    background: var(--paper); color: var(--ink);
  }
  .advert > * { position: absolute; }
  .headline {
    left: 27px; top: 28px;
    font: 600 23px/1 "Montserrat", sans-serif; letter-spacing: 0.2px;
  }
  .address {
    left: 28px; top: 55px;
    font: 500 16px/1 "Montserrat", sans-serif;
  }
  .photo-aerial {
    left: 0; top: 90px; width: 532px; height: 378px;
    background: linear-gradient(160deg, #b9c4c9 0%, #dfe3e2 22%, #8fa39a 45%, #6c7f76 62%, #4f7a3c 80%, #a7b83b 100%);
  }
  .for-sale {
    left: 539px; top: 90px; width: 346px; height: 156px;
    background: var(--pink); color: var(--paper);
    padding: 16px 0 0 19px;
    font: 800 76px/0.86 "Montserrat", sans-serif; letter-spacing: 0;
  }
  .photo-facade {
    left: 539px; top: 251px; width: 346px; height: 217px;
    background: linear-gradient(180deg, #5f93c9 0%, #9cbbd9 35%, #e7e9ea 55%, #cfd3cf 72%, #5e7a3f 100%);
  }
  .summary {
    left: 27px; top: 493px; width: 515px;
    font: 400 23px/1.34 "Roboto Condensed", sans-serif;
  }
  .key-points { list-style: none; }
  .key-points li { position: relative; padding-left: 19px; }
  .key-points li::before {
    content: ""; position: absolute; left: 0; top: 12px;
    width: 9px; height: 9px; background: var(--pink);
  }
  .contact-panel {
    left: 569px; top: 486px; width: 316px; height: 388px;
    background: var(--panel); color: var(--paper);
    font-family: "Roboto Condensed", sans-serif;
  }
  .contact-panel > * { position: absolute; }
  .tender { left: 19px; top: 22px; font-weight: 700; font-size: 20px; }
  .brand-name {
    left: 19px; top: 100px;
    font-weight: 700; font-size: 29px; line-height: 1; letter-spacing: 0.5px;
    color: var(--paper);
  }
  .agent-intro { left: 19px; top: 188px; font-weight: 700; font-size: 19px; line-height: 1.33; }
  .contact-list { left: 17px; top: 242px; list-style: none; font-weight: 700; font-size: 19px; }
  .contact-list li { display: flex; align-items: center; height: 27.5px; }
  .contact-list svg { width: 18px; height: 18px; margin-right: 6px; fill: var(--pink); flex: none; }
</style>
</head>
<body>
<article class="advert">
  <h1 class="headline">MOUNT VICTORIA LAND GRAB</h1>
  <p class="address">Kestrel Lodge, 42 Harwood Terrace, Mount Victoria</p>

  <div class="photo-aerial" role="img" aria-label="Aerial photograph of the white two-storey lodge with its car park and surrounding Mount Victoria houses"></div>
  <div class="for-sale">FOR<br>SALE</div>
  <div class="photo-facade" role="img" aria-label="Photograph of the lodge's white weatherboard side facade with fire escape and garden path"></div>

  <div class="summary">
    <p>This Old Beauty has served many, and is now ripe for development.</p>
    <p>One of Mt Vic's largest land areas, now offered with vacant possession, with key details being:</p>
    <ul class="key-points">
      <li>Large Land area of 2076m² with elevated sunny position and great outlook + access from Pellam Street</li>
      <li>Existing Backpackers Lodge of 970m² providing multiple rooms with amenity areas</li>
      <li>Four adjacent sites also available, taking total land area to 4452m², an unprecedented Land</li>
      <li>Offering in this popular cuity fringe location</li>
    </ul>
  </div>

  <aside class="contact-panel">
    <p class="tender">Now Selling by Closed Tender</p>
    <p class="brand-name">THE VANTREL COLLECTIVE</p>
    <p class="agent-intro">Contact the Sole Agenct :<br>Dean Marlowe</p>
    <ul class="contact-list">
      <li><svg viewBox="0 0 24 24"><path d="M6.6 10.8a15 15 0 0 0 6.6 6.6l2.2-2.2a1 1 0 0 1 1-.25 11.4 11.4 0 0 0 3.6.57 1 1 0 0 1 1 1V20a1 1 0 0 1-1 1A17 17 0 0 1 3 4a1 1 0 0 1 1-1h3.5a1 1 0 0 1 1 1c0 1.25.2 2.45.57 3.570a1 1 0 0 1-.25 1z"/></svg>(04) 555 0182</li>
      <li><svg viewBox="0 0 24 24"><path d="M7 1h10a2 2 0 0 1 2 2v18a2 2 0 0 1-2 2H7a2 2 0 0 1-2-2V3a2 2 0 0 1 2-2zm0 3v14h10V4zm5 15.5a1 1 0 1 0 0 2 1 1 0 0 0 0-2z"/></svg>(021) 555 417</li>
      <li><svg viewBox="0 0 24 24"><path d="M2 5h20v14H2zm2 2v.4l8 5.2 8-5.2V7zm0 2.8V17h16V9.8l-8 5.2z"/></svg>dean@vantrelcollective.co.nz</li>
      <li><svg viewBox="0 0 24 24"><path d="M12 2a10 10 0 1 0 0 20 10 10 0 0 0 0-20zm6.9 6h-3a15 15 0 0 0-1.3-3.9A8 8 0 0 1 18.9 8zM12 4c.8 1.1 1.5 2.5 1.9 4h-3.8c.4-1.5 1.1-2.9 1.9-4zM4.3 14a8 8 0 0 1 0-4h3.4a16 16 0 0 0 0 4zm.8 2h3a15 15 0 0 0 1.3 3.9A8 8 0 0 1 5.1 16zm3-8h-3a8 8 0 0 1 4.3-3.9A15 15 0 0 0 8.1 8zM12 20c-.8-1.1-1.5-2.5-1.9-4h3.8c-.4 1.5-1.1 2.9-1.9 4zm2.3-6H9.7a14 14 0 0 1 0-4h4.6a14 14 0 0 1 0 4zm.3 5.9a15 15 0 0 0 1.3-3.9h3a8 8 0 0 1-4.3 3.9zm1.7-5.9a16 16 0 0 0 0-4h3.4a8 8 0 0 1 0 4z"/></svg>www.vantrelcollective.co.nz</li>
    </ul>
  </aside>
</article>
</body>
</html>
```